We need a logo design that explain all the products we possess.
The main goal is to represent graphically all the logos, pointing to one single logo - Voltane.
The descriptions are in french.
I have uploaded a file with 4 logos to use:
Voltane (the logo that all the rest should be pointing to)
RDM
Parcelin
PattouMou
All logo must be used in the vector graphic format, the description file is in each folder, it's the description that should be next to the logo.

The main goal of this is to create a banner 10' x 11' (estimated)

Target Market(s)

Cities

Requirements
Must have
• All the logos in the zip file in vector graphic.
Nice to have
• A background
Should not have
• Do not use TOB logo, it's a mix with RDM, and Tob Blue/dark blue with inscription "RDM", Charging fees for a part of the picture is not ok!

```html
<!DOCTYPE html>
<html lang="fr">
<head>
<meta charset="utf-8">
<title>Voltane – produits</title>
<link rel="stylesheet" href="https://fonts.googleapis.com/css2?family=Tinos:wght@400&family=Russo+One&family=Montserrat:wght@400;600&display=swap">
<style>
  :root {
    --page: #ffffff;
    --stripe-tone: #eeeff1;
    --blue: #4470b3;
    --red: #cc2229;
    --grey: #a7a8aa;
    --white: #ffffff;
    --hub-light: #e6eef8;
    --hub-mid: #b9cde8;
    --hub-ink: #3e6db3;
    --sky: #62b9ea;
    --grey-ink: #f1f1f1;
  }
  html, body {
    margin: 0;
    padding: 0;
    overflow: hidden;
    background: var(--page);
  }
  .canvas {
    position: relative;
    width: 1200px;
    height: 1091px;
    overflow: hidden;
    background: var(--page);
  }
  .backdrop {
    position: absolute;
    inset: 0;
    background: linear-gradient(135deg, var(--stripe-tone) 0%, var(--page) 50%, var(--stripe-tone) 100%);
  }
  .pyramid {
    position: absolute;
    inset: 0;
  }
  .product-label {
    position: absolute;
    margin: 0;
    white-space: nowrap;
    transform: translateX(-50%);
  }
  .label-rdm {
    left: 600px;
    top: 352px;
    font-family: "Tinos", "Times New Roman", serif;
    font-size: 34px;
    color: var(--white);
    letter-spacing: 1px;
  }
  .label-pattoumou {
    left: 322px;
    top: 880px;
    font-family: "Montserrat", Arial, sans-serif;
    font-weight: 600;
    font-size: 38px;
    color: var(--sky);
  }
  .label-parcelin {
    left: 860px;
    top: 924px;
    font-family: "Montserrat", Arial, sans-serif;
    font-weight: 400;
    font-size: 25px;
    color: var(--grey-ink);
    letter-spacing: 6px;
    text-transform: uppercase;
  }
  .hub {
    position: absolute;
    left: 407px;
    top: 463px;
    width: 366px;
    height: 366px;
    border-radius: 50%;
    border: 10px solid var(--white);
    background: radial-gradient(circle at 50% 45%, var(--hub-light) 0%, var(--hub-mid) 100%);
    display: flex;
    align-items: center;
    justify-content: center;
    gap: 14px;
    box-sizing: content-box;
  }
  .hub-dot {
    width: 34px;
    height: 34px;
    border-radius: 50%;
    background: var(--hub-ink);
  }
  .hub-name {
    font-family: "Russo One", Arial, sans-serif;
    font-size: 50px;
    color: var(--hub-ink);
    letter-spacing: 2px;
    text-transform: uppercase;
  }
</style>
</head>
<body>
  <main class="canvas">
    <div class="backdrop" role="img" aria-label="Fond à fines rayures diagonales grises"></div>

    <svg class="pyramid" width="1200" height="1091" viewBox="0 0 1200 1091" aria-hidden="true">
      <polygon class="face-rdm" points="604,56 387,440 600,640 816,437" fill="var(--blue)" stroke="var(--white)" stroke-width="8" stroke-linejoin="round"/>
      <polygon class="face-pattoumou" points="387,440 64,984 560,984 600,640" fill="var(--red)" stroke="var(--white)" stroke-width="8" stroke-linejoin="round"/>
      <polygon class="face-parcelin" points="816,437 1144,984 512,984 600,700" fill="var(--grey)" stroke="var(--white)" stroke-width="8" stroke-linejoin="round"/>
      <g class="pointer-marks" fill="none" stroke="var(--white)" stroke-width="4" stroke-linejoin="round">
        <polygon points="600,412 568,470 632,470"/>
        <polygon points="413,720 383,780 443,780"/>
        <polygon points="800,720 770,780 830,780"/>
      </g>
    </svg>

    <p class="product-label label-rdm">RDM</p>
    <p class="product-label label-pattoumou">PattouMou</p>
    <p class="product-label label-parcelin">Parcelin</p>

    <div class="hub">
      <span class="hub-dot"></span>
      <span class="hub-name">Voltane</span>
    </div>
  </main>
</body>
</html>
```